Wine Label: Tressivo

The project is to create 3 wine labels. The brand name is "Tressivo"

What we need is to have 3 versions: red wine, white wine and rose.

The wine is for young and modern people, between 21 and 31 years old, so it need to be casual, modern and fun, but at the same time it needs to keep the Premiums of a good European wine.

It is from Italy.

Target Market(s)

Young adults, between 21 and 31 years old. wine lovers

Requirements
Must have
• - Modern colors (Black, silver, red, etc.)
• - Clean label
• - Clear font
• - Style
• - The brand + the type of wine (red, white or rose)
Nice to have
• - A symbol to represent the brand
Should not have
• - Many elements
• - No clear fonts
• - No funny colors

```html
<!DOCTYPE html>
<html lang="en">
<head>
<meta charset="utf-8">
<title>Tressivo Wine Labels</title>
<link rel="stylesheet" href="https://fonts.googleapis.com/css2?family=Courier+Prime:wght@400&display=swap">
<style>
  :root {
    --label-black: #000000;
    --page-white: #ffffff;
    --ink-white: #ffffff;
    --stripe-grey: #9a9a9a;
    --symbol-orange: #f08a2c;
    --symbol-green: #5cc27a;
    --symbol-pink: #e0407a;
    --symbol-violet: #8a5cc8;
  }
  html, body {
    margin: 0;
    padding: 0;
    overflow: hidden;
  }
  body {
    width: 791px;
    height: 1200px;
    background: var(--page-white);
    position: relative;
    font-family: "Courier Prime", "Courier New", monospace;
  }
  .wine-label {
    position: absolute;
    left: 0;
    width: 791px;
    height: 339px;
    background: var(--label-black);
  }
  .wine-label--rose  { top: 0; height: 338px; }
  .wine-label--white { top: 421px; }
  .wine-label--red   { top: 861px; }

  .front-panel {
    position: absolute;
    left: 3px;
    top: 0;
    width: 577px;
    height: 100%;
    border-left: 1px solid var(--stripe-grey);
    box-sizing: border-box;
  }
  .seam-stripe {
    position: absolute;
    top: 0;
    height: 100%;
    width: 6px;
    background: var(--ink-white);
    border-left: 1px solid var(--stripe-grey);
    border-right: 1px solid var(--stripe-grey);
    box-sizing: border-box;
  }
  .seam-stripe--first  { left: 582px; }
  .seam-stripe--second { left: 594px; }

  /* centred column of label content, axis at x = 392 */
  .label-stack {
    position: absolute;
    left: 189px;
    top: 0;
    width: 400px;
    height: 100%;
  }
  .brand-name {
    position: absolute;
    left: 0;
    width: 100%;
    top: 62px;
    text-align: center;
    margin: 0;
    color: var(--ink-white);
    font-size: 52px;
    font-weight: 400;
    letter-spacing: 2px;
    line-height: 1;
  }
  .brand-symbol {
    position: absolute;
    left: 164px;
    top: 134px;
    width: 72px;
    height: 72px;
    background: linear-gradient(135deg, var(--symbol-orange), var(--symbol-pink) 45%, var(--symbol-violet) 70%, var(--symbol-green));
  }
  .wine-type {
    position: absolute;
    left: 0;
    width: 100%;
    top: 254px;
    text-align: center;
    margin: 0;
    color: var(--ink-white);
    font-size: 21px;
    font-weight: 400;
    letter-spacing: 2.5px;
    line-height: 1;
  }
  .origin {
    position: absolute;
    left: 0;
    width: 100%;
    top: 302px;
    text-align: center;
    margin: 0;
    color: var(--ink-white);
    font-size: 11px;
    font-weight: 400;
    letter-spacing: 2px;
    line-height: 1;
  }
</style>
</head>
<body>
  <section class="wine-label wine-label--rose" aria-label="Tressivo Rose label">
    <div class="front-panel"></div>
    <div class="label-stack">
      <h1 class="brand-name">Tressivo</h1>
      <div class="brand-symbol" role="img" aria-label="Brand symbol area"></div>
      <p class="wine-type">Rose</p>
      <p class="origin">Made in Italy</p>
    </div>
    <div class="seam-stripe seam-stripe--first"></div>
    <div class="seam-stripe seam-stripe--second"></div>
  </section>

  <section class="wine-label wine-label--white" aria-label="Tressivo White Wine label">
    <div class="front-panel"></div>
    <div class="label-stack">
      <h2 class="brand-name">Tressivo</h2>
      <div class="brand-symbol" role="img" aria-label="Brand symbol area"></div>
      <p class="wine-type">White Wine</p>
      <p class="origin">Made in Italy</p>
    </div>
    <div class="seam-stripe seam-stripe--first"></div>
    <div class="seam-stripe seam-stripe--second"></div>
  </section>

  <section class="wine-label wine-label--red" aria-label="Tressivo Red Wine label">
    <div class="front-panel"></div>
    <div class="label-stack">
      <h2 class="brand-name">Tressivo</h2>
      <div class="brand-symbol" role="img" aria-label="Brand symbol area"></div>
      <p class="wine-type">Red Wine</p>
      <p class="origin">Made in Italy</p>
    </div>
    <div class="seam-stripe seam-stripe--first"></div>
    <div class="seam-stripe seam-stripe--second"></div>
  </section>
</body>
</html>
```